Free Danish with a coffee offer

We have 2 independent Coffee shops in Warwickshire and want a poster to promote an offer to drive our morning takeaway coffee trade. We compete with the major chains such as Brindle and Moonvale but want to give them a run for their money (and customers) We have great coffee and are local. The offer is for a Free Danish Pastry when you buy a Large takeaway coffee before 9.30am Sunday to Friday

Target Market(s)

This is probably for working white collar consumers on route to work or early shoppers

Industry/Entity Type

Trade

Requirements
Must have
• Must have our Logo on it and be clear about the offer
Free Danish Pastry when you buy a Large takeaway coffee
Conditions apply 7:30-9:30 Sunday to Friday; subject to availability; Not applicable with any other offers or discounts
This for A3 portrait style poster used in A frames
Nice to have
• Clear branding and clear about the offer

```html
<!DOCTYPE html>
<html lang="en">
<head>
<meta charset="utf-8">
<title>Hollin's – Free Danish Pastry</title>
<link href="https://fonts.googleapis.com/css2?family=Ultra&family=Alfa+Slab+One&family=Oswald:wght@500;700&family=Open+Sans:wght@400&display=swap" rel="stylesheet">
<style>
  :root {
    --page: #ffffff;
    --pastry-light: #f3d9a8;
    --pastry-mid: #d9a15a;
    --pastry-dark: #a8622a;
    --green: #1f7a68;
    --heart: #b5002f;
    --heart-edge: #7a0a1e;
    --white: #f7f5f2;
    --orange: #f39a1e;
    --ink: #1f2a24;
    --footer: #f4f4f4;
    --fine: #333333;
  }
  * { margin: 0; padding: 0; box-sizing: border-box; }
  html, body { width: 1200px; height: 900px; overflow: hidden; background: var(--page); }
  .poster {
    position: absolute; left: 280px; top: 0;
    width: 620px; height: 900px; overflow: hidden;
    background: var(--footer);
  }
  .pastry-photo {
    position: absolute; left: 0; top: 0; width: 620px; height: 390px;
    background: radial-gradient(ellipse at 45% 40%, var(--pastry-light) 0%, var(--pastry-mid) 45%, var(--pastry-dark) 100%);
  }
  .green-band {
    position: absolute; left: 0; top: 390px; width: 620px; height: 405px;
    background: var(--green);
  }
  .heart { position: absolute; left: 0; top: 0; width: 620px; height: 900px; }
  .offer { position: absolute; left: 0; width: 620px; text-align: center; white-space: nowrap; }
  .offer-free {
    top: 378px; font-family: "Ultra", "Alfa Slab One", serif; font-size: 140px;
    color: var(--white); line-height: 1.1;
  }
  .offer-item {
    top: 550px; font-family: "Oswald", sans-serif; font-weight: 700;
    font-size: 60px; color: var(--orange); line-height: 1;
  }
  .offer-terms {
    top: 626px; font-family: "Oswald", sans-serif; font-weight: 700;
    font-size: 40px; color: var(--white); line-height: 54px;
  }
  .brand-name {
    position: absolute; font-family: "Oswald", sans-serif; font-weight: 500;
    color: var(--ink); line-height: 1;
  }
  .brand-top { left: 420px; top: 88px; font-size: 46px; }
  .brand-footer { left: 26px; top: 812px; font-size: 42px; }
  .tagline {
    position: absolute; left: 26px; top: 872px;
    font-family: "Open Sans", sans-serif; font-size: 10px;
    color: var(--ink); letter-spacing: 1.5px; text-transform: uppercase;
  }
  .conditions {
    position: absolute; left: 380px; top: 829px; width: 236px;
    font-family: "Open Sans", sans-serif; font-size: 9px;
    line-height: 13px; color: var(--fine);
  }
</style>
</head>
<body>
  <div class="poster">
    <div class="pastry-photo" role="img" aria-label="Close-up photograph of a golden cinnamon Danish pastry dusted with sugar"></div>
    <div class="green-band"></div>

    <svg class="heart" viewBox="0 0 620 900" aria-hidden="true">
      <path d="M310 378 C270 320 200 290 150 295 C60 305 10 370 15 470 C20 600 200 720 310 868 C420 720 600 600 605 470 C610 370 560 305 470 295 C420 290 350 320 310 378 Z"
            fill="var(--heart)" stroke="var(--heart-edge)" stroke-width="4"/>
    </svg>

    <div class="brand-name brand-top">Hollin's</div>

    <div class="offer offer-free">FREE</div>
    <div class="offer offer-item">DANISH PASTRY</div>
    <div class="offer offer-terms">When you order a large<br>takeaway coffee</div>

    <div class="brand-name brand-footer">Hollin's</div>
    <div class="tagline">Local coffee, made with care</div>
    <p class="conditions">Conditions apply 7:30-9:30 Sunday to Friday; subject to availability; Not applicable with any other offers or discounts.</p>
  </div>
</body>
</html>
```